Basic Commercial & Residential Real Estate Web Site

I need a basic website for a new real estate company that deals with both residential and commercial sales. It must be clean and professional. We sell homes, office buildings, farms, and ranches. It should feel crisp and clean.
I need a main page with my logo and links to commercial, residential, farm and land searches with contact data forms. Also incorporated would be a mls property search (IDX) form. I am in Northern California and the current site I posted is at www.tqvandel.com. I need the functionality of the links and the supporting pages. I do not have all the copy ready because I did not know what to expect.
Updates

Project Deadline Extended
Reason: I apologize, I am extremely busy and you all need more data to do a good job. All the designs are great so far and it is extremely difficult to choose at this point. I haven't given you enough data. I haver now uploaded some relevent photos (not very good) and edited the brief. I am looking for what I call the Landing or main page with some functionality built in to other pages which I also need. Example if you click on "Commercial" it should go to a page that discusses our commercial dept.......

I would like to thank all the designers for all their hard work and efforts, I wish I could reward you all.

Thanks again for your creative and professional designs.

Gareth

Target Market(s)

Corporate Execs for the Commercial Buildings
Homeowners/Families for the Homes and Farms
Upper end people for the land to build estates

Industry/Entity Type

Real Estate

Font styles to use
Sans Serif

Requirements
Must have
• Our Logo should be prominent, pronounced
Need contact data or button
Functional Page that links to other data pages
Must Have a "search for properties" feature
Must say "Commercial and Residential Representation"
Pictures of Commercial Building and Nice Home (Tradtional not contemporary)
Nice to have
• Individual Buttons or links to "Commercial, Residential, Farm/Ranch, Land"
Contact Data displayed
button that says "Maple Crest"-next to button is Maple Crest Logo-see www.maplecrestvale.bz
Links to "Buyers and "Sellers"
Links to Facebook, twitter,.....etc
Should not have
• 20+ story commercial buildings or ultra modern. See uploaded files of typical buildings for commercial.

```html
<!DOCTYPE html>
<html lang="en">
<head>
<meta charset="utf-8">
<title>Tqvandel Properties</title>
<link href="https://fonts.googleapis.com/css2?family=Open+Sans:wght@400;600;700&family=PT+Sans+Narrow:wght@700&family=Lora:wght@400&display=swap" rel="stylesheet">
<style>
:root{
  --charcoal:#2b2b2b;
  --charcoal-deep:#1f1f1f;
  --panel-blue:rgba(10,45,95,.82);
  --accent-blue:#2a8fc7;
  --heading-blue:#1b9ad6;
  --olive:#6f8a1a;
  --text:#333;
  --light:#f4f4f4;
  --white:#fff;
  --line:#d8d8d8;
}
*{box-sizing:border-box;margin:0;padding:0}
html,body{width:813px;height:1200px;overflow:hidden}
body{position:relative;background:#f6f6f4;font-family:"Open Sans",sans-serif;color:var(--text)}
.abs{position:absolute}

/* header */
.site-header{left:0;top:0;width:813px;height:88px;background:var(--charcoal)}
.brand{left:68px;top:24px;display:flex;align-items:center;gap:9px;color:var(--white);font-size:22px;font-weight:600;letter-spacing:.3px;line-height:30px}
.brand-mark{width:12px;height:12px;border-radius:50%;background:var(--white)}
.user-links{right:44px;top:22px;font-size:9px;color:var(--olive)}
.user-links span{margin:0 3px;color:#777}
.main-nav{left:380px;top:51px;display:flex;font-size:12px;color:var(--white)}
.main-nav a{color:inherit;text-decoration:none;padding:10px 9px;line-height:15px}
.main-nav a.active{background:var(--white);color:#222}

/* hero */
.hero{left:0;top:88px;width:813px;height:296px;
  background:
    linear-gradient(180deg,rgba(0,0,0,0) 76%,rgba(88,120,58,.95) 90%,#4a6a30 100%),
    linear-gradient(180deg,rgba(255,255,255,0) 0%,rgba(255,255,255,0) 30%,rgba(255,255,255,.25) 31%,rgba(255,255,255,0) 45%),
    linear-gradient(90deg,#38444c 0%,#cfd3d0 12%,#f2f0ea 26%,#b8ab96 34%,#d9d4ca 40%,#eeede9 50%,#2f5fa8 60%,#3a6db4 86%,#4d6b3a 100%)}
.hero-tagline{left:68px;top:326px;background:rgba(20,30,40,.7);color:var(--white);font-size:12px;font-weight:600;letter-spacing:1px;padding:7px 14px}
.hero-arrow{top:226px;width:20px;height:20px;background:rgba(230,230,230,.85);color:#555;font-size:11px;text-align:center;line-height:20px}
.search-panel{left:465px;top:88px;width:286px;height:296px;background:var(--panel-blue);padding:16px 14px 0}
.search-panel h2{text-align:center;color:var(--white);font-size:16px;font-weight:600;margin-bottom:10px}
.search-grid{display:grid;grid-template-columns:1fr 1fr;column-gap:18px}
.field label{display:block;font-size:8px;color:#dde;height:13px}
.field .select{height:20px;background:var(--white);border-radius:2px;font-size:8px;color:#444;padding:5px 10px;position:relative;margin-bottom:16px}
.field .select:after{content:"";position:absolute;right:0;top:0;width:18px;height:20px;border-left:1px solid #ccc;background:#eee}
.field .select:before{content:"";position:absolute;right:5px;top:8px;border:4px solid transparent;border-top:5px solid #444;z-index:1}
.search-btn{margin-top:16px;height:19px;background:var(--accent-blue);color:var(--white);font-size:8px;text-align:center;line-height:19px;border-radius:2px}

/* feature cards */
.card{top:407px;width:197px;height:248px;background:var(--white);box-shadow:0 1px 3px rgba(0,0,0,.25)}
.card .photo{height:160px}
.card .caption{position:absolute;left:0;top:140px;width:100%;height:25px;background:rgba(0,0,0,.55);color:var(--heading-blue);font-size:12px;padding:4px 12px;font-weight:600}
.card p{font-size:8.5px;color:#444;padding:12px 12px 0;line-height:11px}
.read-more{font-size:8.5px;color:var(--olive)}
.card .read-more{position:absolute;right:14px;bottom:12px}
.slide-btn{width:20px;height:22px;background:#111;color:var(--white);font-size:10px;text-align:center;line-height:22px}

/* discussions */
.discussions{left:514px;top:407px;width:233px;height:248px;background:var(--white);box-shadow:0 1px 3px rgba(0,0,0,.25)}
.discussions h3{margin:8px 8px 6px;height:39px;background:var(--light);border-bottom:1px solid var(--line);font-family:"Lora",serif;font-weight:400;font-size:11px;text-align:center;line-height:39px;letter-spacing:.5px}
.post{margin:0 8px 4px;height:39px;border-bottom:1px solid var(--line);position:relative;font-size:8.5px;padding:6px 0 0 46px;line-height:15px}
.post.alt{background:#f0f0f0}
.post .bubble{position:absolute;left:14px;top:9px;width:12px;height:8px;border-radius:50%;background:#777}
.post .meta{display:flex;justify-content:space-between;padding-right:26px}
.post .meta b{font-weight:400;color:var(--olive)}
.view-all{left:570px;top:634px;width:120px;height:21px;background:#444;color:#3f9ad0;font-size:8px;text-align:center;line-height:22px;clip-path:polygon(6% 0,94% 0,100% 100%,0 100%)}

/* work & services */
.section-title{top:683px;font-family:"PT Sans Narrow",sans-serif;font-size:19px;color:var(--heading-blue);padding-bottom:6px;border-bottom:1.5px solid #9ccfe9}
.work-item{top:728px;width:149px}
.work-item .photo{height:108px}
.work-item p,.service p{font-size:8.5px;line-height:15px;margin-top:9px;color:#222}
.work-item .read-more,.service .read-more{float:right}

/* footer */
.site-footer{left:0;top:935px;width:813px;height:237px;background:var(--charcoal)}
.footer-col{top:984px;color:#ddd;font-size:8.5px}
.footer-tag{display:inline-block;background:var(--accent-blue);color:var(--white);font-size:11px;padding:4px 17px;border-radius:2px;margin-bottom:10px}
.footer-col ul{list-style:none}
.footer-col li{height:22px;line-height:22px}
.footer-col li:before{content:"➤";font-size:7px;margin-right:10px;color:#eee}
.blog-entry{line-height:15px;margin-bottom:18px}
.blog-entry a{color:var(--olive);text-decoration:none;border-bottom:1px solid var(--olive);font-size:8px}
.contact-row{display:flex;align-items:center;gap:8px;margin-top:10px}
.socials{display:flex;gap:6px;margin-top:14px}
.socials span{width:14px;height:14px;border-radius:50%}
.copyright{left:0;top:1172px;width:813px;height:28px;background:var(--charcoal-deep);color:#ccc;font-size:7.5px;text-align:center;line-height:28px}
</style>
</head>
<body>

<header class="site-header abs"></header>
<div class="brand abs"><span class="brand-mark"></span>Tqvandel Properties</div>
<div class="user-links abs">Welcome Guest <span>|</span> Login <span>|</span> Register FREE</div>
<nav class="main-nav abs">
  <a class="active">HOME</a><a>COMMERCIAL</a><a>RESIDENTIAL</a><a>FORE</a><a>RENT</a><a>CONTACT</a>
</nav>

<div class="hero abs" role="img" aria-label="Photo of a modern white villa with stone wall, balconies, terrace chairs and lawn under a blue sky"></div>
<div class="hero-tagline abs">COMMERCIAL AND RESIDENTIAL REPRESENTATION</div>
<div class="hero-arrow abs" style="left:0">❮</div>
<div class="hero-arrow abs" style="right:0">❯</div>

<section class="search-panel abs">
  <h2>FIND YOUR NEW HOME</h2>
  <div class="search-grid">
    <div class="field"><label>Type</label><div class="select">Any</div></div>
    <div class="field"><label>City</label><div class="select">Any</div></div>
    <div class="field"><label>Baths</label><div class="select">Any</div></div>
    <div class="field"><label>Status</label><div class="select">Any</div></div>
    <div class="field"><label>State</label><div class="select">Any</div></div>
    <div class="field"><label>Location</label><div class="select">Any</div></div>
    <div class="field"><label>Price From ($)</label><div class="select">Any</div></div>
    <div class="field"><label>Price To ($)</label><div class="select">Any</div></div>
    <div class="field"><label>Beds</label><div class="select">Any</div></div>
    <div class="field"><div class="search-btn">SEARCH</div></div>
  </div>
</section>

<article class="card abs" style="left:68px">
  <div class="photo" role="img" aria-label="Photo of a large traditional estate home beside a pond" style="background:linear-gradient(180deg,#7fb0e3 0%,#c9d6e0 45%,#a7b08a 70%,#6f8fa6 100%)"></div>
  <div class="caption">COMMERCIAL</div>
  <p>Lorem Ipsum is simply dummy text of the printing and typesetting<br>Lorem Ipsum is simply dummy text of the printing and typesetting</p>
  <span class="read-more">Read more.....</span>
</article>
<article class="card abs" style="left:279px">
  <div class="photo" role="img" aria-label="Photo of a glass and brick office building" style="background:linear-gradient(135deg,#d7d9db 0%,#6f6a68 35%,#2e3a44 60%,#8a5a45 100%)"></div>
  <div class="caption">FARM</div>
  <p>Lorem Ipsum is simply dummy text of the printing and typesetting<br>Lorem Ipsum is simply dummy text of the printing and typesetting</p>
  <span class="read-more">Read more.....</span>
</article>
<div class="slide-btn abs" style="left:63px;top:478px">❮</div>
<div class="slide-btn abs" style="left:460px;top:478px">❯</div>

<aside class="discussions abs">
  <h3>LATEST DISCUSSIONS:</h3>
  <div class="post"><span class="bubble"></span>Lorem Ipsum is simply dummy<div class="meta"><span>by : <b>Ipsum</b></span><span>26-03-2014</span></div></div>
  <div class="post alt"><span class="bubble"></span>Lorem Ipsum is simply dummy<div class="meta"><span>by : <b>Ipsum</b></span><span>26-03-2014</span></div></div>
  <div class="post"><span class="bubble"></span>Lorem Ipsum is simply dummy<div class="meta"><span>by : <b>Ipsum</b></span><span>26-03-2014</span></div></div>
  <div class="post alt"><span class="bubble"></span>Lorem Ipsum is simply dummy<div class="meta"><span>by : <b>Ipsum</b></span><span>26-03-2014</span></div></div>
</aside>
<div class="view-all abs">VIEW ALL POSTS</div>

<h2 class="section-title abs" style="left:68px;width:474px">LATEST WORK</h2>
<h2 class="section-title abs" style="left:574px;width:173px">OUR SERVICES</h2>

<div class="work-item abs" style="left:68px">
  <div class="photo" role="img" aria-label="Photo of a low brick office building" style="background:linear-gradient(180deg,#b9cde0 0%,#dfe3e6 35%,#9a5a3e 55%,#8c8c86 100%)"></div>
  <p>Lorem Ipsum is simply dummy text of the printing and typesetting<br>&nbsp;Loremy text the printing and type-settingLoremy text <span class="read-more">Read more...</span></p>
</div>
<div class="work-item abs" style="left:231px">
  <div class="photo" role="img" aria-label="Photo of a traditional estate home beside a pond" style="background:linear-gradient(180deg,#8fb8e6 0%,#d3d8da 45%,#9aa67e 70%,#6d8ea8 100%)"></div>
  <p>Lorem Ipsum is simply dummy text of the printing and typesetting<br>&nbsp;Loremy text the printing and type-settingLoremy text <span class="read-more">Read more...</span></p>
</div>
<div class="work-item abs" style="left:393px">
  <div class="photo" role="img" aria-label="Photo of a two-storey cream family house with a car in the driveway" style="background:linear-gradient(180deg,#9cc3e8 0%,#e8dfc8 40%,#b59a72 70%,#8a8478 100%)"></div>
  <p>Lorem Ipsum is simply dummy text of the printing and typesetting<br>&nbsp;Loremy text the printing and type-settingLoremy text <span class="read-more">Read more...</span></p>
</div>
<div class="slide-btn abs" style="left:63px;top:778px">❮</div>
<div class="slide-btn abs" style="left:527px;top:788px">❯</div>

<div class="service abs" style="left:573px;top:728px;width:174px">
  <div class="photo" role="img" aria-label="Photo of a team of business professionals in suits" style="height:108px;background:linear-gradient(180deg,#f2f2f2 0%,#d8d8d8 50%,#3a3a3e 100%)"></div>
  <p>Lorem Ipsum is simply dummy text of the printing and typesetting<br>&nbsp;Loremy text the printing and typesettin-gLoremy text <span class="read-more">Read more...</span></p>
</div>

<footer class="site-footer abs"></footer>
<div class="footer-col abs" style="left:68px">
  <span class="footer-tag">Quick link</span>
  <ul><li>Home</li><li>Commercial</li><li>Residential</li><li>Fore</li><li>Rent</li><li>Contact</li></ul>
</div>
<div class="footer-col abs" style="left:231px">
  <span class="footer-tag">About Us</span>
  <ul><li>Lorem Ipsum</li><li>Lorem Ipsum</li><li>Lorem Ipsum</li><li>Lorem Ipsum</li><li>Lorem Ipsum</li><li>Lorem Ipsum</li></ul>
</div>
<div class="footer-col abs" style="left:393px;width:150px">
  <span class="footer-tag" style="padding:4px 30px">Blog</span>
  <div class="blog-entry">Lorem Ipsum is simply dummy text of the printing and typesetting<br><a>industry's standard industry's stan-</a></div>
  <div class="blog-entry">Lorem Ipsum is simply dummy text of the printing and typesetting<br><a>industry's standard dard</a></div>
</div>
<div class="footer-col abs" style="left:602px;width:160px">
  <span class="footer-tag">Contact Us</span>
  <div style="line-height:14px">Lorem Ipsum is simply dummy text of the printing and typesetting<br>of the printing and typesetting</div>
  <div class="contact-row" style="margin-top:16px">
    <svg width="8" height="10" viewBox="0 0 8 10"><path d="M2 0h2v3H3v4h1v3H2C0 8 0 2 2 0z" fill="#eee"/></svg>
    <span>: +1-530-555-0147</span>
  </div>
  <div class="contact-row">
    <svg width="12" height="8" viewBox="0 0 12 8"><rect x=".5" y=".5" width="11" height="7" fill="none" stroke="#eee"/><path d="M.5 .5L6 5 11.5 .5" fill="none" stroke="#eee"/></svg>
    <span>: desk@tqvandel.com</span>
  </div>
  <div class="socials">
    <span style="background:#3b5998"></span><span style="background:#2aa9e0"></span><span style="background:#0e76a8"></span><span style="background:#dd4b39"></span>
  </div>
</div>
<div class="copyright abs">Copyright © 2014 . All rights reserved.</div>

</body>
</html>
```